Business Card design
Cordavera Ruvek Martial Arts Training Center
I need single sided standard sized Business Card [3.5" x 2"]
Font in logo is CGF Locust Resistance. This font does not need to be used.
Modern
Cordavera Ruvek or Cordavera Ruvek Martial Arts Training Center
Martial Arts Discipline | Athletic Excellence
2671 Bramble Rd
Kalamazoo, MI
info@cordaverix.example
www.cordaverix.example
facebook.com/cordaverix
optional items for the business card:
Pelnor Grappling League
Todd Weslin Jiu Jitsu
Orvane Kickboxing Union
Mixed Martial Arts
Fitness
Can put the logo on one side and the information on the second side if you would like to submit that type of design.
Cordavera Ruvek illustrator file
Cordavera Ruvek eps file

```html
<!DOCTYPE html>
<html lang="en">
<head>
<meta charset="utf-8">
<title>Cordavera Ruvek – Business Card</title>
<link href="https://fonts.googleapis.com/css2?family=Open+Sans:wght@400;600;700;800&display=swap" rel="stylesheet">
<style>
  :root {
    --brand-red: #e8413a;
    --brand-red-dark: #c9302a;
    --card-white: #ffffff;
    --band-grey: #c9c9c9;
    --ink-grey: #6b6b6b;
    --ink-dark: #4a4a4a;
    --canvas-bg: #e4e4e4;
  }
  * { margin: 0; padding: 0; box-sizing: border-box; }
  html, body {
    width: 1200px; height: 862px; overflow: hidden;
    background: var(--canvas-bg);
    font-family: "Open Sans", Arial, sans-serif;
  }
  .sheet {
    position: relative; width: 1200px; height: 862px;
    display: flex; align-items: center; justify-content: center; gap: 40px;
  }
  .card {
    position: relative; width: 520px; height: 297px; overflow: hidden;
    box-shadow: 0 6px 18px rgba(0,0,0,.18);
  }
  .card-front { background: var(--card-white); }
  .card-back { background: var(--brand-red); display: flex; align-items: center; justify-content: center; }

  .edge-bands { position: absolute; left: 0; width: 100%; height: 30px; }
  .edge-bands--top { top: 0; }
  .edge-bands--bottom { bottom: 0; }

  .brand-lockup { display: flex; align-items: center; gap: 8px; }
  .brand-mark { width: 14px; height: 14px; }
  .brand-name { font-weight: 800; letter-spacing: .5px; text-transform: uppercase; }

  .front-logo {
    position: absolute; top: 44px; left: 0; width: 100%;
    display: flex; flex-direction: column; align-items: center;
  }
  .front-logo .brand-mark { background: var(--ink-dark); }
  .front-logo .brand-name { color: var(--ink-dark); font-size: 24px; }
  .tagline { margin-top: 3px; font-size: 7px; color: var(--ink-grey); font-style: italic; }

  .center-title {
    position: absolute; top: 108px; left: 0; width: 100%; text-align: center;
    color: var(--brand-red); font-weight: 700; font-size: 11.5px;
  }

  .faint-emblem {
    position: absolute; right: 70px; top: 70px; width: 56px; height: 56px;
    border-radius: 50%; background: #f1f1f1;
  }

  .contact-block {
    position: absolute; left: 26px; top: 150px;
    font-size: 8.5px; line-height: 13px; color: var(--ink-grey);
  }
  .contact-block .label { color: var(--brand-red); font-weight: 700; display: inline-block; width: 12px; }
  .contact-gap { height: 9px; }

  .address-line {
    position: absolute; left: 26px; bottom: 42px;
    font-size: 9px; font-weight: 600; color: var(--brand-red);
  }

  .back-logo .brand-mark { background: var(--card-white); width: 22px; height: 22px; }
  .back-logo .brand-name { color: var(--card-white); font-size: 34px; }
</style>
</head>
<body>
<main class="sheet">
  <section class="card card-front" aria-label="Business card front">
    <svg class="edge-bands edge-bands--top" viewBox="0 0 520 30" preserveAspectRatio="none" aria-hidden="true">
      <polygon points="0,0 520,0 520,10 0,10" fill="var(--band-grey)"/>
      <polygon points="0,0 150,0 135,14 0,14" fill="var(--brand-red)"/>
      <polygon points="420,0 520,0 520,8 428,8" fill="var(--brand-red)"/>
    </svg>

    <div class="faint-emblem" aria-hidden="true"></div>

    <div class="front-logo">
      <div class="brand-lockup">
        <span class="brand-mark"></span>
        <span class="brand-name">Cordavera Ruvek</span>
      </div>
      <p class="tagline">Martial Arts Discipline | Athletic Excellence</p>
    </div>

    <p class="center-title">Cordavera Ruvek or Cordavera Ruvek Martial Arts Training Center</p>

    <div class="contact-block">
      <p><span class="label">P</span> +1 269 555 0142</p>
      <p><span class="label">F</span> +1 269 555 0178</p>
      <p><span class="label">M</span> +1 269 555 0193</p>
      <div class="contact-gap"></div>
      <p><span class="label">E</span> info@cordaverix.example</p>
      <p><span class="label">W</span> www.cordaverix.example</p>
    </div>

    <p class="address-line">Suite 4, Level 2, 2671 Bramble Rd, Kalamazoo, MI</p>

    <svg class="edge-bands edge-bands--bottom" viewBox="0 0 520 30" preserveAspectRatio="none" aria-hidden="true">
      <polygon points="0,20 520,20 520,30 0,30" fill="var(--band-grey)"/>
      <polygon points="0,24 360,24 372,30 0,30" fill="var(--brand-red)"/>
      <polygon points="470,16 520,16 520,30 480,30" fill="var(--brand-red)"/>
    </svg>
  </section>

  <section class="card card-back" aria-label="Business card back">
    <div class="brand-lockup back-logo">
      <span class="brand-mark"></span>
      <span class="brand-name">Cordavera Ruvek</span>
    </div>
  </section>
</main>
</body>
</html>
```